Founder / concept developer needs business card // Consultant needs VCARD

I need a business card for me as a founding consultant in Berlin. I advise entrepreneurs, especially in the design of business ideas, business plans or financing applications. More information about this in the annexes. My USP: I design / structure complex ideas and projects convincingly so that my client is successful. I want to communicate professionalism, effectiveness and clarity. Colors like from the range BLACK-GRAY-GREEN. I am 27 years old, I have studied business for 7 years. Attachments: - Business card design (only idea, do not focus on it) - Website screenshot (only idea, do not focus on it)

Target Market(s)

Target group: Founder (20-50 yrs, m / w, needy, in "break-up phase") and CONTRACTOR / "financier" (30-55 yrs, m / w, often public service "routine-oriented"). The foundations are in quite different industries: digital, craft, tourism, retail, services, etc. Almost all German.

Industry/Entity Type

Consultant

Contact Information for Business Card

Lukas Brenner
M. Sc., International Business Administration
Gründungsberater, Konzeptentwickler
www.falkor-plan.de
kontakt@falkor-plan.de
Tel. 0157 284 3361

Colors

Designer to choose colors to be used in the design.

Requirements
Must have
• Professionalism, persuasiveness, clarity
Nice to have
• memorability
Should not have
• Schnörkelei

```html
<!DOCTYPE html>
<html lang="de">
<head>
<meta charset="utf-8">
<title>Lukas Brenner – Visitenkarte</title>
<link rel="stylesheet" href="https://fonts.googleapis.com/css2?family=Montserrat:wght@300;400;500;600&display=swap">
<style>
  :root {
    --backdrop: #1d1d1d;
    --card-light: #f2f2f2;
    --card-dark: #0c0c0c;
    --ink: #1a1a1a;
    --ink-inverse: #f4f4f4;
    --accent: #5bb89c;
    --card-radius: 18px;
  }
  * { box-sizing: border-box; margin: 0; padding: 0; }
  html, body {
    width: 1200px;
    height: 410px;
    overflow: hidden;
    background: var(--backdrop);
    font-family: "Montserrat", Arial, sans-serif;
  }
  .card-set {
    width: 1200px;
    height: 410px;
    display: flex;
    align-items: center;
    justify-content: space-around;
    padding: 0 50px;
  }
  .card {
    width: 470px;
    height: 276px;
    border-radius: var(--card-radius);
    position: relative;
  }
  .card--front {
    background: var(--card-light);
    display: flex;
    align-items: center;
    justify-content: center;
  }
  .wordmark {
    display: flex;
    align-items: center;
    font-weight: 600;
    font-size: 19px;
    letter-spacing: 0.22em;
    color: var(--ink);
    text-transform: uppercase;
  }
  .wordmark__first { padding-right: 4px; }
  .wordmark__last {
    background: var(--accent);
    padding: 6px 6px 6px 10px;
  }
  .card--back {
    background: var(--card-dark);
    color: var(--ink-inverse);
    display: flex;
    align-items: center;
    padding-left: 70px;
  }
  .contact-list { list-style: none; }
  .contact-list__item {
    display: flex;
    align-items: center;
    gap: 18px;
    font-weight: 300;
    font-size: 13px;
    letter-spacing: 0.02em;
    height: 36px;
  }
  .contact-list__icon {
    width: 22px;
    height: 22px;
    flex: none;
    fill: none;
    stroke: var(--ink-inverse);
    stroke-width: 1.3;
    stroke-linecap: round;
    stroke-linejoin: round;
  }
</style>
</head>
<body>
<main class="card-set">
  <section class="card card--front" aria-label="Vorderseite">
    <h1 class="wordmark">
      <span class="wordmark__first">Lukas</span>
      <span class="wordmark__last">Brenner</span>
    </h1>
  </section>

  <section class="card card--back" aria-label="Rückseite">
    <ul class="contact-list">
      <li class="contact-list__item">
        <svg class="contact-list__icon" viewBox="0 0 22 22" aria-hidden="true">
          <rect x="5" y="2.5" width="12" height="17" rx="1"/>
          <path d="M8 7h6M8 10h6M8 13h6M8 16h4"/>
        </svg>
        <span>M. Sc. International Business Administration</span>
      </li>
      <li class="contact-list__item">
        <svg class="contact-list__icon" viewBox="0 0 22 22" aria-hidden="true">
          <circle cx="11" cy="7.5" r="4"/>
          <path d="M4 19.5c0-4 3-6.5 7-6.5s7 2.5 7 6.5z"/>
        </svg>
        <span>Founder, Concept Developer</span>
      </li>
      <li class="contact-list__item">
        <svg class="contact-list__icon" viewBox="0 0 22 22" aria-hidden="true">
          <path d="M8 3.5l2 4-2 1.5c.8 2.2 2.3 3.9 4.5 5l1.5-2 4 2-1.5 3.5C10.5 17 5.5 11.5 5 5z"/>
        </svg>
        <span>0157 284 3361</span>
      </li>
      <li class="contact-list__item">
        <svg class="contact-list__icon" viewBox="0 0 22 22" aria-hidden="true">
          <circle cx="11" cy="11" r="8"/>
          <ellipse cx="11" cy="11" rx="3.5" ry="8"/>
          <path d="M3 11h16M4.5 7h13M4.5 15h13"/>
        </svg>
        <span>www.falkor-plan.de</span>
      </li>
      <li class="contact-list__item">
        <svg class="contact-list__icon" viewBox="0 0 22 22" aria-hidden="true">
          <rect x="2.5" y="5" width="17" height="12" rx="1"/>
          <path d="M2.5 5.5l8.5 6.5 8.5-6.5"/>
        </svg>
        <span>kontakt@falkor-plan.de</span>
      </li>
    </ul>
  </section>
</main>
</body>
</html>
```